Brochure Design Project

hi
Im looking for a great little design for my brochures. I have a home beauty salon and need a brochure menu. The name of the business is Kanoha SoftGlow which is a japanese name. I'm not japanese but want it to have a slight feel of japanese, perhaps some watercolour or a traditional pattern.
Salon menu will have waxing, Facials, massage etc and would like a tri fold brochure
No bright colours please or butterflies. I want it to look and feel relaxing and peaceful. Help with a nice Logo would also be great
thanks for your help
Updates

Project Deadline Extended
Reason: I know a lot of you are busy but by extending the timeframe I can hopefully get all your creative minds flowing

hi

Just thought I'd add that I would like the brochures to be modern and edgy looking
thanks so far

Target Market(s)

People that want to be pampered and look and feel great and have a sort of natural feel ( if that makes sense)

Industry/Entity Type

Beauty Salon

Requirements
Must have
• I would like it to be A4 size and folded as a tri brochure,
Nice to have
• A classy font
Should not have
• Butterflies, swirls, bright colours or purple

```html
<!DOCTYPE html>
<html lang="en">
<head>
<meta charset="utf-8">
<title>Kanoha SoftGlow – Treatment Menu</title>
<link rel="stylesheet" href="https://fonts.googleapis.com/css2?family=Great+Vibes&family=Exo+2:ital,wght@0,600;1,400&display=swap">
<style>
  :root{
    --wash-peach:#f6c9a4;
    --wash-rose:#f2b2a6;
    --wash-cream:#fbe6cf;
    --wash-gold:#f3cf8f;
    --panel:rgba(255,246,236,0.55);
    --maroon:#8e1b2a;
    --ink:#7d1d25;
    --dot:#9a2a35;
    --photo-a:#c98f6a;
    --photo-b:#f0dfd0;
  }
  *{box-sizing:border-box;margin:0;padding:0}
  html,body{width:1200px;height:848px;overflow:hidden;background:#fff}
  .brochure{
    position:relative;width:1200px;height:848px;overflow:hidden;
    background:
      radial-gradient(ellipse at 10% 8%, var(--wash-rose) 0%, transparent 45%),
      radial-gradient(ellipse at 92% 12%, var(--wash-gold) 0%, transparent 40%),
      radial-gradient(ellipse at 85% 92%, var(--wash-rose) 0%, transparent 45%),
      radial-gradient(ellipse at 20% 95%, var(--wash-peach) 0%, transparent 50%),
      linear-gradient(135deg, var(--wash-peach), var(--wash-cream) 45%, var(--wash-peach));
    font-family:"Exo 2",sans-serif;color:var(--ink);
  }
  .panel{position:absolute;left:30px;top:30px;width:1150px;height:790px;background:var(--panel)}
  .edge-dots{position:absolute;left:0;top:826px;width:1200px;border-top:3px dotted var(--dot)}
  .section-title{
    position:absolute;font-family:"Great Vibes",cursive;font-weight:400;color:var(--maroon);
    font-size:64px;line-height:1;
  }
  .title-facials{left:50px;top:50px}
  .title-massage{left:846px;top:50px}
  .photo{position:absolute;border:2px dotted var(--dot);padding:3px}
  .photo span{display:block;width:100%;height:100%;background:linear-gradient(135deg,var(--photo-a),var(--photo-b))}
  .photo-facial{left:51px;top:131px;width:337px;height:182px}
  .photo-stone{left:869px;top:137px;width:237px;height:172px}
  .photo-brush{left:694px;top:336px;width:137px;height:185px}
  .photo-back{left:973px;top:651px;width:196px;height:154px}
  .treatment{position:absolute;font-size:13px;line-height:17px}
  .treatment h3{font-weight:600;font-size:14px;line-height:18px;color:var(--maroon)}
  .treatment p{font-style:italic;margin-top:16px}
  .treatment h3 + p{margin-top:27px}
  .treatment .allow{font-weight:600;font-style:normal;margin-top:17px}
  .treatment h3 + .allow{margin-top:8px}
  .left{left:51px;width:337px}
  .mid{left:416px;width:362px}
  .mid-narrow{left:416px;width:272px}
  .right{left:841px;width:310px}
  .divider{position:absolute;border-top:3px dotted var(--dot)}
</style>
</head>
<body>
<div class="brochure">
  <div class="panel"></div>

  <h2 class="section-title title-facials">Facials</h2>
  <div class="photo photo-facial"><span role="img" aria-label="Photo of a client in a white robe relaxing during a face mask treatment"></span></div>

  <article class="treatment left" style="top:329px">
    <h3>Kiyora Facial - $40.00<br>Series of 3 - $105.00</h3>
    <p>When time is of the essence, this Express Facial treatment will revitalise your skin's radiance, leaving it with a healthy glow.</p>
    <p>Includes cleansing, exfoliation, pressure point massage, moisturiser and sunscreen.</p>
    <p class="allow">Allow 30 min</p>
  </article>
  <div class="divider" style="left:51px;top:542px;width:337px"></div>
  <article class="treatment left" style="top:550px">
    <h3>Vitamin C Facial Brightening Treatment - $70.00<br>Series of 3 - $190.00</h3>
    <p>This facial treatment uses a concentrated complex of topical vitamin C that is easily absorbed by the skin. This helps battle the visible signs of ageing.</p>
    <p>This formulation has been proven in the medical field to be an antioxidant that works by mopping up damaging chemical compounds known as "free radicals." This topical antioxidant also stimulates the production of collagen.</p>
    <p class="allow">Allow 1 hr</p>
  </article>

  <article class="treatment mid" style="top:48px">
    <h3>Kanoha Signature Facial - $75.00<br>Series of 3 - $200.00</h3>
    <p>Enjoy an hour of total relaxation and emerge looking and feeling great!</p>
    <p>This facial is the ultimate for the over worked and over stressed. Your customised facial will begin with a deep cleanse, followed by a gentle exfoliation, mask, massage and completed with a nourishing moisturizer and eye crème.</p>
    <p class="allow">Allow 1 hr</p>
  </article>
  <div class="divider" style="left:416px;top:295px;width:268px"></div>
  <article class="treatment mid-narrow" style="top:307px">
    <h3>Vitamin C Facial Brightening Treatment - $70.00<br>Series of 3 - $190.00</h3>
    <p>This blissful treatment starts with a dry body brush, jojoba oil is then drizzled over the back, followed by a completely relaxing hot stone back massage. To finish off, your skin is treated to a indugently nourishing facial.</p>
    <p class="allow">Allow 1 hr 15 min</p>
  </article>
  <div class="photo photo-brush"><span role="img" aria-label="Photo of a therapist giving a dry body brush treatment on the back"></span></div>
  <div class="divider" style="left:416px;top:514px;width:268px"></div>
  <article class="treatment mid" style="top:528px">
    <h3>Kanoha Man - $70.00<br>Series of 3 - $190.00</h3>
    <p>Maintain the vitality and look of healthy skin with a double cleanse, exfoliate facial massage, and a hydrating mask.</p>
  </article>
  <article class="treatment mid" style="top:666px">
    <h3>Bare Back Purification - $50.00</h3>
    <p>This includes a deep cleanse. Exfoliation, extractions, mask and moisturizer to leave your back feeling smooth and refreshed.</p>
    <p class="allow">Allow 30min</p>
  </article>

  <h2 class="section-title title-massage">Massage</h2>
  <div class="photo photo-stone"><span role="img" aria-label="Photo of a client lying face down with smooth stones along the back"></span></div>
  <article class="treatment right" style="top:316px">
    <h3>Full body Hot Stone Massage - $85.00</h3>
    <p>This treatment melts away tension with smooth warm basalt stones and will put you in the ultimate relaxed state.</p>
    <p class="allow">Allow 1 hr</p>
  </article>
  <div class="divider" style="left:841px;top:453px;width:263px"></div>
  <article class="treatment right" style="top:469px">
    <h3>Body massage - $60.00</h3>
    <p>Relaxing the body as well as the mind will rejuvenate and awaken your spirit. Choose a Relaxation, Swedish or Aromatherapy massage.</p>
    <p class="allow">Allow 1 hr</p>
  </article>
  <div class="divider" style="left:841px;top:603px;width:263px"></div>
  <article class="treatment right" style="top:622px">
    <h3>Back Massage - $50.00</h3>
    <p class="allow">Allow 1/2 hr</p>
  </article>
  <div class="photo photo-back"><span role="img" aria-label="Photo of a man receiving a shoulder massage"></span></div>

  <div class="edge-dots"></div>
</div>
</body>
</html>
```